Need a Logo & Website PSD for Marlow Turf Fields

I need a PSD for Marlow Turf Fields website.
I also need a logo design vector.

The farm is located in Louisville KY.
here is the current website, it is extremely plain and boring.
Marlow Turf Fields
http://marlowturffieldsco.greenexample.net/

Anything Goes!!
Show me what you have!!

```html
<!DOCTYPE html>
<html lang="en">
<head>
<meta charset="utf-8">
<title>Marlow Turf Fields</title>
<link rel="stylesheet" href="https://fonts.googleapis.com/css2?family=Ubuntu:wght@400;500;700&family=Roboto+Condensed:wght@700&display=swap">
<style>
:root{
  --green-dark:#3f7f05;
  --green:#4a8e08;
  --green-bright:#63b012;
  --green-line:#2f6703;
  --lime:#a6e55a;
  --lime-light:#c9f48e;
  --page:#eefbdc;
  --page-band:#e5f8cb;
  --text-green:#3bb21e;
  --heading:#1f7a14;
  --footer-link:#9fdc57;
  --white:#ffffff;
}
*{box-sizing:border-box;margin:0;padding:0}
html,body{width:1133px;height:1200px;overflow:hidden}
body{position:relative;background:var(--page);font-family:"Ubuntu",sans-serif}

.top-strip{position:absolute;left:0;top:0;width:1133px;height:63px;background:var(--white)}
.top-strip svg{position:absolute;left:0;top:0}
.login-form{position:absolute;top:18px;left:462px;display:flex;gap:10px;align-items:center}
.login-form .field{width:175px;height:27px;border:1px solid #8da78a;background:linear-gradient(#f4f7f3,#c7d3c5)}
.login-form .field + .field{margin-left:0}
.login-form .btn{height:26px;padding:0 13px;font-size:12px;font-weight:500;color:var(--white);display:flex;align-items:center;border:1px solid #2b6a05;background:linear-gradient(#78c421,#3e8a08)}
.login-form .btn.signup{background:linear-gradient(#4d9a0d,#2c6d03)}

.header{position:absolute;left:0;top:63px;width:1133px;height:94px;background:linear-gradient(var(--green-bright),var(--green-dark));border-top:2px solid var(--green-line);border-bottom:2px solid var(--green-line)}
.brand{position:absolute;left:206px;top:22px;display:flex;align-items:center;gap:10px}
.brand .dot{width:40px;height:40px;border-radius:50%;background:var(--lime)}
.brand .name{font-size:40px;color:var(--lime-light);font-weight:500}
.live-chat{position:absolute;left:775px;top:12px;display:flex;align-items:center;gap:7px;color:var(--white);font-size:13px}
.social{position:absolute;left:885px;top:15px;display:flex;gap:6px}
.social span{width:13px;height:13px;background:#dfe9f2;border-radius:2px}
.search{position:absolute;left:776px;top:49px;display:flex}
.search .field{width:148px;height:24px;border:1px solid #2c6c05;background:linear-gradient(#fbfcfa,#cbd6c8)}
.search .go{width:34px;height:24px;background:#2c6c05;display:flex;align-items:center;justify-content:center}

.panel{position:absolute;left:164px;top:199px;width:806px}
.nav{height:47px;background:linear-gradient(#3e8a06,#62b514);display:flex;align-items:center;padding-left:31px;font-size:15px;font-weight:500;color:var(--white)}
.nav a{color:var(--white);text-decoration:none}
.nav .sep{margin:0 15px}
.hero{position:relative;height:337px;background:radial-gradient(ellipse at 30% 35%,#d6f9a6 0%,#b2ec72 45%,#97dc55 100%);overflow:hidden}
.hero-copy{position:absolute;left:0;top:76px;width:420px;text-align:center;color:var(--heading);font-family:"Roboto Condensed",sans-serif;font-weight:700}
.hero-copy h1{font-size:35px;line-height:1.05;padding-left:30px}
.hero-copy h2{font-size:24px;line-height:1.3}
.hero-copy p{font-size:17px;color:#1d5a10;margin-top:4px}
.hero .signup{position:absolute;left:121px;top:203px;width:130px;height:34px;border-radius:4px;background:linear-gradient(#f8fff0,#b7ec6f);border:1px solid #9ad25c;color:#2f7a15;font-size:14px;display:flex;align-items:center;justify-content:center;box-shadow:0 3px 4px rgba(60,110,20,.35)}
.video{position:absolute;left:418px;top:45px;width:371px;height:243px;background:var(--white);padding:6px;box-shadow:0 8px 8px rgba(40,90,10,.3)}
.video .media{width:100%;height:100%;background:linear-gradient(135deg,#4f8f26,#2f6a14 60%,#5b9d2a);position:relative}
.video .play{position:absolute;left:50%;top:50%;transform:translate(-50%,-50%)}
.hero-shadow{height:14px;background:radial-gradient(ellipse at 50% 0,rgba(120,160,90,.45),rgba(0,0,0,0) 70%)}

.membership{position:absolute;left:0;top:620px;width:1133px}
.membership h3{position:absolute;left:172px;top:0;font-size:26px;font-weight:500;color:var(--heading)}
.membership .band{position:absolute;left:0;top:37px;width:1133px;height:182px;background:var(--page-band)}
.membership .photo{position:absolute;left:171px;top:50px;width:226px;height:150px;background:linear-gradient(160deg,#3d7a20,#1f4d12 50%,#6aa83a);border:1px solid #2d5e1a}
.membership .copy{position:absolute;left:415px;top:44px;width:555px;font-size:13.4px;line-height:19px;color:var(--text-green)}
.membership .copy strong{color:#1f8a16;font-weight:700}
.membership .copy p + p{margin-top:12px}

.footer{position:absolute;left:0;top:890px;width:1133px;height:212px;background:var(--green);border-top:2px solid var(--green-line)}
.footer .col{position:absolute;top:35px}
.footer .company{left:173px}
.footer .company h4{font-size:20px;font-weight:400;color:var(--white)}
.footer .company p{font-size:11px;color:var(--footer-link);margin-top:14px}
.footer .divider{position:absolute;top:36px;width:0;height:156px;border-left:1px dashed #6aa82e}
.footer .links{left:506px}
.footer .links h5{font-size:13px;font-weight:500;color:var(--white);margin-bottom:10px;margin-top:3px}
.footer .links li{list-style:none;font-size:11px;color:var(--footer-link);line-height:21px}
.footer .quote{left:745px;font-size:20px;color:#e8ffd0;line-height:27px}
.footer .quote span{color:#c8f27a}
.copyright{position:absolute;left:0;top:1102px;width:1133px;height:92px;background:var(--green);border-top:1px solid #5aa418;text-align:center;color:#eaf8dc;font-size:10px;line-height:20px;padding-top:8px}
.base{position:absolute;left:0;top:1194px;width:1133px;height:6px;background:var(--white)}
</style>
</head>
<body>

<div class="top-strip">
  <svg width="1133" height="63" viewBox="0 0 1133 63" aria-hidden="true">
    <polygon points="422,0 1013,0 970,63 466,63" fill="#4a8e08"/>
    <rect x="0" y="0" width="1133" height="6" fill="#3f7f05"/>
  </svg>
  <div class="login-form">
    <div class="field"></div>
    <div class="field"></div>
    <div class="btn">Login</div>
    <div class="btn signup">Signup</div>
  </div>
</div>

<header class="header">
  <div class="brand"><span class="dot"></span><span class="name">Marlow Turf Fields</span></div>
  <div class="live-chat">
    <svg width="24" height="18" viewBox="0 0 24 18" aria-hidden="true"><ellipse cx="12" cy="8" rx="11" ry="7" fill="#fff"/><polygon points="6,13 4,18 11,14" fill="#fff"/></svg>
    Live Chat
  </div>
  <div class="social"><span></span><span></span><span></span><span></span></div>
  <div class="search">
    <div class="field"></div>
    <div class="go">
      <svg width="18" height="16" viewBox="0 0 18 16" aria-hidden="true"><circle cx="6" cy="6" r="4.5" fill="none" stroke="#fff" stroke-width="2"/><line x1="9.5" y1="9" x2="16" y2="14" stroke="#fff" stroke-width="3"/></svg>
    </div>
  </div>
</header>

<main class="panel">
  <nav class="nav">
    <a href="#">Home</a><span class="sep">|</span>
    <a href="#">About Us</a><span class="sep">|</span>
    <a href="#">Services</a><span class="sep">|</span>
    <a href="#">Location</a><span class="sep">|</span>
    <a href="#">Contact Us</a>
  </nav>
  <section class="hero">
    <div class="hero-copy">
      <h1>Lorem ipsum dolor sit amet,</h1>
      <h2>consectetuer adipiscing elit.</h2>
      <p>Aliquam tincidunt mauris eu risus.</p>
    </div>
    <div class="signup">Sign up</div>
    <div class="video">
      <div class="media" role="img" aria-label="Video still of hands trimming a green hedge with garden shears">
        <svg class="play" width="84" height="84" viewBox="0 0 84 84" aria-hidden="true">
          <circle cx="42" cy="42" r="40" fill="rgba(70,140,170,.45)" stroke="rgba(255,255,255,.35)" stroke-width="2"/>
          <polygon points="32,24 62,42 32,60" fill="rgba(255,255,255,.6)"/>
        </svg>
      </div>
    </div>
  </section>
  <div class="hero-shadow"></div>
</main>

<section class="membership">
  <h3>Membership In Organizations</h3>
  <div class="band"></div>
  <div class="photo" role="img" aria-label="Photo of a lush green forest path"></div>
  <div class="copy">
    <p>Sod can be a great alternative to the hassle of maintaining grass or other greenery! Let <strong>Marlow Turf Fields, Inc.</strong> be the company you choose to provide you with the best sod in the city! Whether you need a large amount of sod or just enough to cover the area in your yard, we can handle the job. We offer great prices on sod and related services and we guarantee quality no matter what.</p>
    <p>Read on to learn more about what we can do for you, or call us at <strong>502-555-0148</strong> to schedule your sod service.</p>
  </div>
</section>

<footer class="footer">
  <div class="col company">
    <h4>Marlow Turf Fields, Inc.</h4>
    <p>1420 Meadow Rd &nbsp;| Louisville, KY 40291</p>
    <p>Phone: 502-555-0148</p>
  </div>
  <div class="divider" style="left:400px"></div>
  <div class="col links">
    <h5>About us</h5>
    <ul><li>Home</li><li>About Us</li><li>Services</li><li>Location</li><li>Contact Us</li></ul>
  </div>
  <div class="divider" style="left:678px"></div>
  <div class="col quote">For a quote on services,<br><span>call:502-555-0148.</span></div>
</footer>

<div class="copyright">
  © 2013 &nbsp;Fieldline Media LLC. All rights reserved. FM, the FM logo and all other FM marks contained herein<br>
  are trademarks of Fieldline Media LLC and/or FM affiliated companies. All other marks contained herein are<br>
  the property of their respective owners.
</div>
<div class="base"></div>

</body>
</html>
```